Bluefen Assist Re-Design\ Add Hosting Content

We are redesigning our web site. We have already picked out the Corvinel WordPress Hosting theme. All content will come from our current website and go onto the new website. http://www.bluefen-assist-hq.net . This website will interface with WHMCS billing software. I have attached old logos as well as icons for the hosting theme which is also attached.

Target Market(s)

Tech, Web, Hosting

Industry/Entity Type

Tech

Logo Text

Bluefen Assist, "The New IT Department"

```html
<!DOCTYPE html>
<html lang="en">
<head>
<meta charset="utf-8">
<title>Bluefen Assist – The New IT Department</title>
<link href="https://fonts.googleapis.com/css2?family=Roboto:wght@300;400;500;700&display=swap" rel="stylesheet">
<style>
:root{
  --red:#e0161f;
  --red-dark:#b80d14;
  --ink:#2b2b2b;
  --text:#555;
  --muted:#8a8a8a;
  --dark:#2a2a2d;
  --darker:#222326;
  --footer:#333538;
  --light:#efefef;
  --line:#d9d9d9;
  --white:#fff;
}
*{box-sizing:border-box;margin:0;padding:0}
html,body{width:1200px;height:2594px;overflow:hidden}
body{font-family:'Roboto',Arial,sans-serif;color:var(--text);background:var(--white);position:relative}
.wrap{position:absolute;left:268px;width:666px}
a{color:inherit;text-decoration:none}

/* header */
.site-header{position:absolute;top:0;left:0;width:1200px;height:52px;background:var(--white);border-bottom:1px solid #e5e5e5}
.brand{position:absolute;left:268px;top:8px;display:flex;align-items:center;gap:8px}
.brand-mark{width:34px;height:34px;background:var(--red)}
.brand-name{font-size:13px;font-weight:700;color:var(--ink);line-height:1.1}
.brand-name small{display:block;font-size:8px;font-weight:400;color:var(--muted)}
.main-nav{position:absolute;left:452px;top:0;height:52px;display:flex}
.main-nav a{font-size:9px;text-transform:uppercase;color:#555;padding:0 10px;height:52px;line-height:52px;border-left:1px solid #e5e5e5}
.main-nav a.active{color:var(--ink);font-weight:500}
.main-nav a:last-child{border-right:1px solid #e5e5e5}
.header-phone{position:absolute;left:846px;top:16px;display:flex;align-items:center;gap:8px;font-size:10px;color:var(--ink)}

/* hero */
.hero{position:absolute;top:52px;left:0;width:1200px;height:358px;background:linear-gradient(110deg,#8d8c8c 0%,#c9c7c7 35%,#b3a9ab 65%,#7e7878 100%)}
.hero::after{content:"";position:absolute;inset:0;background:rgba(40,40,40,.35)}
.hero-copy{position:absolute;left:268px;top:98px;z-index:2;color:var(--white);font-weight:300}
.hero-copy .l1{font-size:44px;line-height:50px}
.hero-copy .l2{font-size:31px;line-height:36px;font-weight:700;color:var(--red)}
.hero-copy .l3{font-size:31px;line-height:36px}
.hero-list{position:absolute;left:612px;top:80px;z-index:2;list-style:none}
.hero-list li{display:flex;align-items:center;gap:16px;height:52px;margin-bottom:19px;font-size:19px;font-weight:300;color:var(--white)}
.hero-icon{width:52px;height:52px;border-radius:50%;background:var(--red);border:3px solid var(--white);display:flex;align-items:center;justify-content:center}
.hero-arrow{position:absolute;top:160px;width:32px;height:32px;border:2px solid var(--white);border-radius:50%;z-index:2;display:flex;align-items:center;justify-content:center}

/* shop bar */
.shop-bar{position:absolute;top:410px;left:0;width:1200px;height:76px;background:var(--dark)}
.shop-bar p{position:absolute;left:318px;top:16px;width:330px;text-align:center;color:#e8e8e8;font-size:16px;line-height:21px;font-weight:300}
.shop-bar b{font-weight:700}
.btn-outline-light{position:absolute;left:676px;top:24px;width:92px;height:26px;border:1px solid var(--white);color:var(--white);font-size:10px;text-align:center;line-height:24px;text-transform:uppercase}

/* intro */
.intro-title{top:514px;font-size:17px;font-weight:300;color:#444}
.intro-title b{color:var(--red);font-weight:500}
.feature{position:absolute;top:568px;width:214px}
.feature-head{display:flex;align-items:center;gap:12px;height:46px;font-size:11px;color:var(--ink)}
.feature p{margin-top:20px;font-size:8.5px;line-height:13.8px;color:#666}
.btn-outline-red{display:block;margin-top:20px;width:92px;height:25px;border:1px solid var(--red);color:var(--red);font-size:9px;text-align:center;line-height:23px;text-transform:uppercase}

/* consultation */
.consult{position:absolute;top:788px;left:0;width:1200px;height:291px;background:linear-gradient(100deg,#3a3a3e 0%,#5b3a3d 45%,#8a2a30 70%,#3f3a3c 100%)}
.consult h2{position:absolute;left:268px;top:46px;color:var(--white);font-size:19px;font-weight:700}
.consult h3{position:absolute;left:268px;top:70px;color:var(--white);font-size:16px;font-weight:300}
.field{position:absolute;left:268px;width:325px;height:25px;border:1px solid #aaa;background:rgba(0,0,0,.2);color:#ddd;font-size:8.5px;line-height:23px;padding-left:14px}
.btn-red{position:absolute;left:268px;top:228px;width:95px;height:26px;background:var(--red);color:var(--white);font-size:9px;text-align:center;line-height:26px;text-transform:uppercase}
.consult-photo{position:absolute;left:631px;top:12px;width:277px;height:279px;background:linear-gradient(180deg,#d9c9bf 0%,#eeeeee 55%,#d5dbe0 100%);border-radius:120px 120px 0 0}

/* services */
.section-title{position:absolute;left:0;width:1200px;text-align:center}
.services-title{top:1119px;font-size:19px;font-weight:700;color:var(--ink)}
.services-sub{top:1142px;font-size:16px;font-weight:300;color:#666}
.service-card{position:absolute;top:1193px;width:152px;height:225px;background:linear-gradient(180deg,var(--red) 0%,var(--red-dark) 100%);color:var(--white);text-align:center}
.service-badge{width:110px;height:110px;margin:14px auto 0;border-radius:50%;border:3px solid var(--white);display:flex;align-items:center;justify-content:center}
.service-badge span{width:96px;height:96px;border-radius:50%;background:var(--white);display:flex;align-items:center;justify-content:center}
.service-card p{margin-top:29px;font-size:13px;line-height:15px;font-weight:300}
.dots{position:absolute;display:flex;gap:3px}
.dots i{width:10px;height:10px;border-radius:50%;background:var(--red)}
.dots i.off{background:var(--white);border:2px solid var(--red)}

/* stats */
.stats{position:absolute;top:1513px;left:0;width:1200px;height:214px;background:linear-gradient(90deg,#2f2b2c 0%,#4a4244 50%,#2f2b2c 100%)}
.stat{position:absolute;top:50px;width:116px;height:112px;border:1px solid #cfcfcf;color:var(--white);text-align:center;font-size:13px;line-height:15px;font-weight:300}
.stat svg{display:block;margin:14px auto 8px}

/* testimonials and news */
.block-title{position:absolute;top:1771px;font-size:19px;font-weight:700;color:var(--ink)}
.quote{position:absolute;left:268px;top:1812px;width:323px;height:118px;background:var(--light);padding:18px 20px 0 24px}
.quote .mark{font-size:24px;color:var(--red);font-weight:700;line-height:12px;display:block}
.quote p{margin-top:6px;font-size:8.3px;line-height:12.7px;color:#555;padding-left:6px}
.author{position:absolute;left:268px;top:1947px;display:flex;gap:12px}
.author-pic{width:57px;height:57px;border:1px solid var(--line);display:flex;align-items:center;justify-content:center}
.author-pic span{width:24px;height:24px;background:var(--red)}
.author-name{font-size:11px;font-weight:700;color:var(--red);margin-top:8px}
.author-role{font-size:8.5px;line-height:12px;color:#777}
.news{position:absolute;left:609px;width:324px;height:52px;padding:8px 12px}
.news-dark{top:1815px;background:var(--darker);border:2px solid var(--red)}
.news-line{top:1879px;border:2px solid #f0a9ab}
.news h4{font-size:14px;font-weight:700}
.news-dark h4{color:var(--white)}
.news-line h4{color:var(--red)}
.news small{font-size:8px;color:#999}
.news-dark small{color:#bbb}
.news-more{position:absolute;left:609px;top:1955px;font-size:8.5px;color:#666;line-height:12px}
.news-more b{color:var(--red);font-weight:500;font-size:10px}

/* contact bar */
.contact-bar{position:absolute;top:2052px;left:0;width:1200px;height:130px;background:var(--light)}
.contact-bar h2{position:absolute;top:26px;width:1200px;text-align:center;font-size:20px;font-weight:300;color:#555}
.contact-row{position:absolute;top:70px;left:0;width:1200px;display:flex;justify-content:center;align-items:center;gap:20px;font-size:15px;color:var(--ink)}
.or{width:38px;height:38px;border-radius:50%;border:2px solid var(--red);text-align:center;line-height:34px;font-size:12px}

/* social band */
.social-band{position:absolute;top:2182px;left:0;width:1200px;height:118px;background:var(--dark)}
.social-col{position:absolute;top:0;height:118px;width:170px;text-align:center;color:var(--white);font-size:9px;line-height:12px;padding-top:19px}
.social-col + .social-col{border-left:1px solid #444}
.social-dot{display:block;width:36px;height:36px;border-radius:50%;background:var(--red);border:2px solid var(--white);margin:0 auto 8px}
.social-col small{display:block;font-size:6.5px;color:#aaa;margin-top:2px}
.pill{display:inline-block;width:28px;height:10px;background:#d8d8d8;margin-top:4px;border-radius:2px}

/* footer */
.site-footer{position:absolute;top:2300px;left:0;width:1200px;height:249px;background:var(--footer);color:#bbb}
.footer-col{position:absolute;top:40px}
.footer-col h5{font-size:10px;font-weight:700;color:var(--white);margin-bottom:26px}
.footer-col ul{list-style:none;font-size:8.5px;line-height:13.3px}
.contact-list li{display:flex;gap:8px;margin-bottom:12px;line-height:12px}
.contact-list i{width:7px;height:7px;border-radius:50%;background:var(--red);margin-top:3px;flex:none}
.follow-grid{display:grid;grid-template-columns:repeat(2,20px);gap:8px 9px}
.follow-grid span{width:20px;height:20px;border-radius:50%;border:1px solid #888}
.footer-brand{display:flex;align-items:center;gap:8px;margin-bottom:10px}
.footer-brand span{width:36px;height:36px;background:#666}
.footer-brand b{font-size:13px;color:var(--white);line-height:1.1}
.footer-brand b small{display:block;font-size:8px;font-weight:400;color:#aaa}
.footer-about{width:200px;font-size:8.3px;line-height:12.5px}
.badges{display:flex;gap:8px;margin-top:10px}
.badges span{width:72px;height:36px;background:#1d5e95;border:2px solid var(--white)}
.badges span + span{background:#d9d9d9;border-color:var(--red)}

/* bottom bar */
.bottom-bar{position:absolute;top:2549px;left:0;width:1200px;height:45px;background:var(--darker)}
.bottom-bar p{position:absolute;left:268px;top:17px;font-size:8px;color:var(--red)}
.bottom-nav{position:absolute;right:266px;top:0;display:flex}
.bottom-nav a{font-size:9px;color:#ccc;padding:0 12px;height:45px;line-height:45px;border-left:1px solid #444}
</style>
</head>
<body>

<header class="site-header">
  <div class="brand">
    <span class="brand-mark"></span>
    <span class="brand-name">Bluefen Assist<small>The New IT Department</small><small>Bluefen-Assist-HQ.net</small></span>
  </div>
  <nav class="main-nav">
    <a class="active">Home</a><a>Service</a><a>Business Users</a><a>Home Users</a><a>About Us</a><a>Contact</a>
  </nav>
  <div class="header-phone">
    <svg width="20" height="20" viewBox="0 0 20 20"><circle cx="10" cy="10" r="9" fill="none" stroke="#e0161f" stroke-width="1.5"/><path d="M6.5 6c0 4.5 3 7.5 7.5 7.5l1-1.8-2-1.2-1 1c-1.3-.5-2.4-1.6-3-3l1-1-1.2-2z" fill="#e0161f"/></svg>
    (555) 014-2290
  </div>
</header>

<section class="hero" role="img" aria-label="Blurred photo of a desk with a stethoscope and a hand at a keyboard">
  <div class="hero-arrow" style="left:19px"><svg width="10" height="12" viewBox="0 0 10 12"><path d="M7 1L2 6l5 5" fill="none" stroke="#fff" stroke-width="2"/></svg></div>
  <div class="hero-arrow" style="left:1147px"><svg width="10" height="12" viewBox="0 0 10 12"><path d="M3 1l5 5-5 5" fill="none" stroke="#fff" stroke-width="2"/></svg></div>
  <div class="hero-copy">
    <div class="l1">Whatever Your</div>
    <div class="l2">Business Needs Are</div>
    <div class="l3">Bluefen Assist Has</div>
    <div class="l3">You Covered</div>
  </div>
  <ul class="hero-list">
    <li><span class="hero-icon"><svg width="22" height="22" viewBox="0 0 22 22"><rect x="3" y="4" width="16" height="5" fill="#fff"/><rect x="3" y="11" width="16" height="5" fill="#fff"/></svg></span>Online Backup Solutions</li>
    <li><span class="hero-icon"><svg width="24" height="24" viewBox="0 0 24 24"><circle cx="12" cy="12" r="10" fill="#fff"/><path d="M12 12V2a10 10 0 0 1 10 10z" fill="#f5b400"/><path d="M12 12h10a10 10 0 0 1-12 9.8z" fill="#2a66c9"/></svg></span>Malware Prevention &amp; Cleanup</li>
    <li><span class="hero-icon"><svg width="22" height="22" viewBox="0 0 22 22"><path d="M7 10V7a4 4 0 0 1 8 0v3" fill="none" stroke="#f5c300" stroke-width="2"/><rect x="5" y="10" width="12" height="9" fill="#f5c300"/></svg></span>Secure Monitoring</li>
  </ul>
</section>

<section class="shop-bar">
  <p>Bluefen Assist now offers on-line ordering.<br>Visit <b>BA Shop</b> to find out more.</p>
  <a class="btn-outline-light">BA Shop</a>
</section>

<h2 class="wrap intro-title">Bluefen Assist Is The IT Support Solution To Your <b>Business &amp; Home</b> Needs!</h2>

<article class="feature" style="left:268px">
  <div class="feature-head"><svg width="54" height="44" viewBox="0 0 54 44"><rect x="2" y="2" width="50" height="32" fill="#2d6fb4" stroke="#333" stroke-width="2"/><rect x="20" y="34" width="14" height="6" fill="#888"/><rect x="14" y="40" width="26" height="3" fill="#666"/></svg>$50 Flat Rate Repair</div>
  <p>When it comes to business, IT is an absolute must. However, hiring your own IT employees isn't. BA can provide industry proven expertise for your business at a fraction of the cost of hiring your own IT support department.</p>
  <a class="btn-outline-red">Learn More</a>
</article>
<article class="feature" style="left:494px">
  <div class="feature-head"><svg width="34" height="46" viewBox="0 0 34 46"><rect x="2" y="2" width="30" height="42" fill="#3a3a3a"/><g fill="#999"><rect x="6" y="7" width="22" height="4"/><rect x="6" y="15" width="22" height="4"/><rect x="6" y="23" width="22" height="4"/><rect x="6" y="31" width="22" height="4"/></g></svg>Online Backup</div>
  <p>VaultR offers you and your business a variety of data backup solutions to fit your specific needs. For non-commercial backup of your personal files, check out the simplicity of VaultR.</p>
  <a class="btn-outline-red">Learn More</a>
</article>
<article class="feature" style="left:721px">
  <div class="feature-head"><svg width="46" height="34" viewBox="0 0 46 34"><rect x="2" y="2" width="42" height="30" fill="#fff" stroke="#e0161f" stroke-width="2" stroke-dasharray="4 3"/><path d="M4 4l19 15L42 4" fill="none" stroke="#999" stroke-width="1.5"/></svg>Email Solutions</div>
  <p>Email designed with Business and Home users in mind. Experience a clean, fast Webmail with powerful features for your business and home needs. Learn how our mail solutions can help your business.</p>
  <a class="btn-outline-red">Learn More</a>
</article>

<section class="consult">
  <h2>Free Consultations</h2>
  <h3>Receive a FREE Consultation Now!</h3>
  <div class="field" style="top:108px">Your Name (required)</div>
  <div class="field" style="top:146px">Your Email (required)</div>
  <div class="field" style="top:184px">Phone</div>
  <a class="btn-red">Send</a>
  <div class="consult-photo" role="img" aria-label="Photo of a smiling doctor in a white coat with a stethoscope"></div>
</section>

<h2 class="section-title services-title">Services</h2>
<p class="section-title services-sub">Lorem Ipsum is simply dummy text</p>

<div class="service-card" style="left:268px">
  <div class="service-badge"><span><svg width="46" height="46" viewBox="0 0 46 46"><rect x="8" y="4" width="30" height="38" fill="#333"/><g fill="#888"><rect x="12" y="8" width="22" height="3"/><rect x="12" y="14" width="22" height="3"/><rect x="12" y="20" width="22" height="3"/><rect x="12" y="26" width="22" height="3"/><rect x="12" y="32" width="22" height="3"/></g></svg></span></div>
  <p>Data Backup<br>&amp; Recovery</p>
</div>
<div class="service-card" style="left:439px">
  <div class="service-badge"><span><svg width="46" height="46" viewBox="0 0 46 46"><path d="M8 38L30 16" stroke="#e0161f" stroke-width="6" stroke-linecap="round"/><path d="M10 10l26 26" stroke="#999" stroke-width="5" stroke-linecap="round"/><circle cx="33" cy="13" r="7" fill="none" stroke="#999" stroke-width="4"/></svg></span></div>
  <p>Repair &amp;<br>Diagnostics</p>
</div>
<div class="service-card" style="left:609px">
  <div class="service-badge"><span><svg width="46" height="46" viewBox="0 0 46 46"><circle cx="23" cy="23" r="18" fill="#333"/><circle cx="23" cy="23" r="12" fill="#3f8f3a"/><path d="M23 23L33 13" stroke="#f5c300" stroke-width="2"/><circle cx="23" cy="23" r="3" fill="#e0161f"/></svg></span></div>
  <p>Virus &amp; Malware<br>Protection</p>
</div>
<div class="service-card" style="left:778px">
  <div class="service-badge"><span><svg width="50" height="36" viewBox="0 0 50 36"><rect x="2" y="2" width="46" height="32" fill="#f4f4f4" stroke="#bbb" stroke-width="1.5"/><path d="M3 3l22 17L47 3" fill="none" stroke="#999" stroke-width="1.5"/></svg></span></div>
  <p>Email<br>Setup</p>
</div>
<div class="dots" style="left:583px;top:1446px"><i></i><i class="off"></i><i></i></div>

<section class="stats" role="img" aria-label="Dark photo of server rack cabling behind the figures">
  <div class="stat" style="left:268px"><svg width="38" height="30" viewBox="0 0 38 30"><path d="M10 26a8 8 0 0 1 0-16 10 10 0 0 1 19 1 7 7 0 0 1 0 15z" fill="#fff"/><path d="M19 11v10m-4-4l4 4 4-4" stroke="#2f2b2c" stroke-width="2" fill="none"/></svg>Data<br>Transfered</div>
  <div class="stat" style="left:451px"><svg width="30" height="32" viewBox="0 0 30 32"><rect x="3" y="2" width="18" height="24" fill="#fff"/><rect x="9" y="6" width="18" height="24" fill="#fff" stroke="#2f2b2c" stroke-width="1.5"/><g stroke="#2f2b2c" stroke-width="1.5"><path d="M12 12h12M12 16h12M12 20h12M12 24h8"/></g></svg>Files<br>Hosted</div>
  <div class="stat" style="left:633px"><svg width="34" height="30" viewBox="0 0 34 30"><g fill="none" stroke="#fff" stroke-width="2"><rect x="2" y="2" width="8" height="26"/><rect x="13" y="2" width="8" height="26"/><rect x="24" y="2" width="8" height="26"/></g></svg>Pages<br>Served</div>
  <div class="stat" style="left:814px"><svg width="32" height="32" viewBox="0 0 32 32"><circle cx="16" cy="16" r="13" fill="none" stroke="#fff" stroke-width="2"/><circle cx="11" cy="13" r="1.8" fill="#fff"/><circle cx="21" cy="13" r="1.8" fill="#fff"/><path d="M9 19a8 8 0 0 0 14 0" fill="none" stroke="#fff" stroke-width="2"/></svg>Happy<br>Clients</div>
</section>

<h2 class="block-title" style="left:268px">What Our Clients Say</h2>
<h2 class="block-title" style="left:609px">Recent News</h2>
<blockquote class="quote">
  <span class="mark">&ldquo;</span>
  <p>Lorem Ipsum is simply dummy text of the printing and typesetting industry. Lorem Ipsum has been the industry's standard dummy text ever since the 1500s, when an unknown printer took a galley of type and scrambled it to make a type specimen book. It has survived not only five centuries, but also the leap into electronic typesetting, remaining essentially</p>
</blockquote>
<div class="author">
  <div class="author-pic"><span></span></div>
  <div><div class="author-name">Paul Venner CEO &amp;</div><div class="author-role">Founder Holtmark Labs<br>www.holtmarklabs.net</div></div>
</div>
<div class="dots" style="left:556px;top:1954px"><i></i><i class="off"></i><i></i></div>
<div class="news news-dark"><h4>Innovations in Education</h4><small>May 27, 2014 &nbsp; Dana &nbsp; Articles</small></div>
<div class="news news-line"><h4>Innovations in Education</h4><small>May 27, 2014 &nbsp; Dana &nbsp; Articles</small></div>
<div class="news-more">Follow<br><b>Continue Reading......</b></div>

<section class="contact-bar">
  <h2>Contact a Bluefen Assist professional in Dunmere today at</h2>
  <div class="contact-row"><span>(555) 014-2290</span><span class="or">OR</span><span>info@bluefen-assist-hq.net.</span></div>
</section>

<section class="social-band">
  <div class="social-col" style="left:268px;width:161px"><span class="social-dot"></span>Follow us Blog</div>
  <div class="social-col" style="left:429px;width:169px"><span class="social-dot"></span>We are on Facelink Like<br>us to see our daily updates!<br><span class="pill"></span></div>
  <div class="social-col" style="left:598px;width:170px"><span class="social-dot"></span>@bluefenassist<br>Greetings, my friend<small>Posted 47 days ago via Chirper mobile</small></div>
  <div class="social-col" style="left:768px;width:166px"><span class="social-dot"></span>We are on Circlenet +<br>Visit our Page<br><span class="pill"></span></div>
</section>

<footer class="site-footer">
  <div class="footer-col" style="left:268px">
    <h5>Quick Links</h5>
    <ul>
      <li>- About Bluefen Assist</li><li>- Our Partners</li><li>- Terms &amp; Conditions</li><li>- Privacy Policy</li><li>- Certifications</li><li>- Testimonials</li><li>- News</li><li>- Security Alerts</li><li>- Contact Us</li><li>- Sitemap</li>
    </ul>
  </div>
  <div class="footer-col" style="left:437px">
    <h5>Dunmere, Westvale</h5>
    <ul class="contact-list">
      <li>Bluefen Assist, LLC.</li>
      <li><i></i><span>4120 Larkmoor Road, Ste 210<br>Dunmere, Westvale 60412</span></li>
      <li><i></i>(555) 014-2290</li>
      <li><i></i>info@bluefen-assist-hq.net</li>
      <li><i></i>http://www.bluefen-assist-hq.net</li>
    </ul>
  </div>
  <div class="footer-col" style="left:609px">
    <h5>Follow us</h5>
    <div class="follow-grid"><span></span><span></span><span></span><span></span><span></span><span></span><span></span><span></span></div>
  </div>
  <div class="footer-col" style="left:735px;top:30px">
    <div class="footer-brand"><span></span><b>Bluefen Assist<small>The New IT Department</small></b></div>
    <p class="footer-about">At Bluefen Assist, we began our company with the idea of providing superior online technical support, affordable computer repair and managed service solutions to businesses and home consumers, using the best practices and technology in the industry, for the least cost.</p>
    <div class="badges"><span></span><span></span></div>
  </div>
</footer>

<div class="bottom-bar">
  <p>&copy; 2014 Bluefen Assist. All rights reserved.</p>
  <nav class="bottom-nav"><a>Home</a><a>Service</a><a>Business Users</a><a>Home Users</a><a>About Us</a><a>Contact</a></nav>
</div>

</body>
</html>
```